4 Poster Designs required for Nail Salon

We require 4 poster designs that will be displayed inside a shopping centre. Each design should contain our logo and the words "Located next to TallMart" (or similar). Design 1 (MOTHERS DAY) should contain the words "Mothers Day Special" and "$10 gift voucher when you spend over $50". Design 2 (CHRISTMAS) should contain the words "Christmas in July" and "Purchase a set of nails and get a $10 gift voucher". Design 3 (ALL YEAR) should contain the words "New Deluxe Spa Pedicure Service" and the words "Try our new Deluxe Spa Pedicure and get a free nail buff, shape and polish for your fingernails". Design 4 (ALL YEAR 2)should contain high quality nail salon image(s) and the words "Now Open". We like designs that support our image of high quality/fun/clean and safe.
Updates
I will close this early. In 24 hours.
Target Market(s)
Rich mums
Industry/Entity Type
Shopping
Look and feel
Each slider illustrates characteristics of the customer's brand and the style your logo design should communicate.

```html
<!DOCTYPE html>
<html lang="en">
<head>
<meta charset="utf-8">
<title>Whisper Nail Salon – Mother's Day Special</title>
<link rel="stylesheet" href="https://fonts.googleapis.com/css2?family=Pinyon+Script&family=Poppins:ital,wght@0,300;1,300;1,600&family=Arimo:wght@700&display=swap">
<style>
  :root {
    --bg-deep: #ee5fc9;
    --bg-mid: #f590dc;
    --bg-light: #fcd3f1;
    --title-pink: #dc1478;
    --offer-yellow: #f7ea6e;
    --offer-shadow: rgba(150, 40, 110, 0.45);
    --brand-white: #ffffff;
    --sparkle: #ffffff;
    --band-pink: #f7bde3;
    --band-line: #ffffff;
    --band-text: #111111;
    --floral-top: #f3a6d6;
    --floral-bottom: #9fbf78;
  }

  * { margin: 0; padding: 0; box-sizing: border-box; }

  html, body {
    width: 848px;
    height: 1200px;
    overflow: hidden;
  }

  .poster {
    position: relative;
    width: 848px;
    height: 1200px;
    overflow: hidden;
    background:
      radial-gradient(ellipse at 95% 5%, var(--bg-light) 0%, rgba(252,211,241,0) 45%),
      linear-gradient(165deg, var(--bg-deep) 0%, var(--bg-mid) 55%, var(--bg-light) 100%);
  }

  .sparkles {
    position: absolute;
    top: 0;
    left: 0;
    width: 848px;
    height: 1200px;
  }

  .sparkles line {
    stroke: var(--sparkle);
    stroke-linecap: round;
  }

  .brand {
    position: absolute;
    top: 78px;
    left: 0;
    width: 848px;
    text-align: center;
    color: var(--brand-white);
    font-family: 'Poppins', sans-serif;
    font-weight: 300;
  }

  .brand__name {
    display: block;
    font-size: 56px;
    letter-spacing: 8px;
    line-height: 1;
    padding-left: 40px;
  }

  .brand__tagline {
    display: block;
    font-size: 16px;
    letter-spacing: 2px;
    margin-top: 8px;
    padding-left: 250px;
  }

  .headline {
    position: absolute;
    left: 0;
    width: 848px;
    text-align: center;
    font-family: 'Pinyon Script', cursive;
    color: var(--title-pink);
    text-shadow: 0 0 6px #ffffff, 0 0 12px rgba(255,255,255,0.8);
    line-height: 1;
    white-space: nowrap;
  }

  .headline--occasion { top: 262px; font-size: 112px; }
  .headline--special  { top: 432px; font-size: 126px; }

  .offer {
    position: absolute;
    top: 638px;
    left: 0;
    width: 848px;
    text-align: center;
    font-family: 'Poppins', sans-serif;
    font-style: italic;
    font-weight: 300;
    font-size: 50px;
    line-height: 72px;
    color: var(--offer-yellow);
    text-shadow: 2px 2px 3px var(--offer-shadow);
  }

  .offer strong { font-weight: 600; }

  .floral-border {
    position: absolute;
    top: 815px;
    left: 0;
    width: 848px;
    height: 258px;
    background: linear-gradient(180deg, rgba(243,166,214,0) 0%, var(--floral-top) 30%, var(--floral-bottom) 100%);
  }

  .location-band {
    position: absolute;
    top: 1070px;
    left: 0;
    width: 848px;
    height: 80px;
    background: var(--band-pink);
    border-top: 8px solid var(--band-line);
    border-bottom: 6px solid var(--band-line);
    display: flex;
    align-items: center;
    justify-content: center;
    font-family: 'Arimo', sans-serif;
    font-weight: 700;
    font-size: 27px;
    color: var(--band-text);
  }
</style>
</head>
<body>
  <main class="poster">
    <svg class="sparkles" viewBox="0 0 848 1200" aria-hidden="true">
      <defs>
        <g id="glint">
          <line x1="-14" y1="0" x2="14" y2="0" stroke-width="1.5" opacity="0.9"/>
          <line x1="0" y1="-14" x2="0" y2="14" stroke-width="1.5" opacity="0.9"/>
          <line x1="-5" y1="-5" x2="5" y2="5" stroke-width="1" opacity="0.6"/>
          <line x1="-5" y1="5" x2="5" y2="-5" stroke-width="1" opacity="0.6"/>
        </g>
      </defs>
      <use href="#glint" x="612" y="58"/>
      <use href="#glint" x="700" y="110"/>
      <use href="#glint" x="760" y="40"/>
      <use href="#glint" x="805" y="160"/>
      <use href="#glint" x="540" y="160"/>
      <use href="#glint" x="395" y="200"/>
      <use href="#glint" x="650" y="230"/>
      <use href="#glint" x="780" y="255"/>
      <use href="#glint" x="520" y="435"/>
      <use href="#glint" x="460" y="470"/>
      <use href="#glint" x="735" y="540"/>
      <use href="#glint" x="805" y="575"/>
      <use href="#glint" x="690" y="610"/>
      <use href="#glint" x="120" y="590"/>
      <use href="#glint" x="60" y="660"/>
      <use href="#glint" x="160" y="700"/>
      <use href="#glint" x="430" y="610"/>
      <use href="#glint" x="800" y="700"/>
      <use href="#glint" x="300" y="790"/>
      <use href="#glint" x="590" y="800"/>
      <use href="#glint" x="90" y="785"/>
      <use href="#glint" x="720" y="790"/>
    </svg>

    <header class="brand">
      <span class="brand__name">Whisper</span>
      <span class="brand__tagline">Nail Salon</span>
    </header>

    <h1>
      <span class="headline headline--occasion">Mother's Day</span>
      <span class="headline headline--special">Special</span>
    </h1>

    <p class="offer">
      <strong>$10</strong> gift voucher<br>
      when you spend over <strong>$50</strong>
    </p>

    <div class="floral-border" role="img" aria-label="Border of pink and yellow roses with green leaves and pale pink blossoms"></div>

    <footer class="location-band">We are located next to TallMart</footer>
  </main>
</body>
</html>
```